Business Card Design Project

A double sided business card for presentation to business leaders in corporate.

Target Market(s)

Corporate, business professionals, HR

Industry/Entity Type

Business

Requirements
Must have
• FRONT

Logo

www.brightfernco.com.au

BACK

Maren Tollvey-Hart
Director

+ 61 (0) 418 556 230
maren@brightfernco.com.au
www.brightfernco.com.au

Impact through energy and employee engagement

("ripples" of logo, bottom corner)

Must be:
- double sided
size: 86 x 54mm
supplied as one pdf with crop marks shown (+- 1mm, with 2-3 mm bleed)

```html
<!DOCTYPE html>
<html lang="en">
<head>
<meta charset="utf-8">
<title>Bright Fern Co – Business Card</title>
<link rel="stylesheet" href="https://fonts.googleapis.com/css2?family=Arimo:ital,wght@0,400;0,700;1,700&display=swap">
<style>
  :root {
    --backdrop: #1f1f20;
    --card-dark: #4b4b4d;
    --card-light: #fbfbfb;
    --brand-plum: #7b2870;
    --ink-grey: #555558;
    --ink-dark: #2a2a2c;
    --white: #ffffff;
  }
  * { box-sizing: border-box; margin: 0; padding: 0; }
  html, body {
    width: 1200px;
    height: 900px;
    overflow: hidden;
    background: var(--backdrop);
    font-family: "Arimo", Arial, sans-serif;
  }
  .canvas {
    position: relative;
    width: 1200px;
    height: 900px;
  }
  .card {
    position: absolute;
    left: 340px;
    width: 520px;
    height: 326px;
    border-radius: 3px;
    box-shadow: 0 10px 30px rgba(0,0,0,0.45);
    overflow: hidden;
  }
  .card--front {
    top: 100px;
    background: var(--card-dark);
  }
  .card--back {
    top: 470px;
    background: var(--card-light);
  }

  /* Front */
  .front-brand {
    position: absolute;
    left: 0;
    right: 0;
    top: 118px;
    text-align: center;
  }
  .wordmark {
    display: inline-flex;
    align-items: center;
    gap: 14px;
    font-size: 50px;
    font-weight: 400;
    letter-spacing: -0.5px;
    line-height: 1;
  }
  .wordmark__dot {
    width: 16px;
    height: 16px;
    border-radius: 50%;
    background: currentColor;
  }
  .front-brand .wordmark { color: var(--white); }
  .front-url {
    position: absolute;
    right: 96px;
    top: 192px;
    color: var(--white);
    font-size: 14px;
    letter-spacing: 0.2px;
  }
  .front-url strong { font-weight: 700; }

  /* Back */
  .back-brand {
    position: absolute;
    left: 40px;
    top: 44px;
  }
  .back-brand .wordmark {
    color: var(--brand-plum);
    font-size: 40px;
    gap: 12px;
  }
  .back-brand .wordmark__dot { width: 13px; height: 13px; }
  .contact {
    position: absolute;
    left: 44px;
    top: 178px;
    color: var(--ink-dark);
  }
  .contact__name {
    color: var(--brand-plum);
    font-size: 19px;
    font-weight: 700;
  }
  .contact__role {
    color: var(--ink-grey);
    font-size: 14px;
    margin-top: 2px;
  }
  .contact__list {
    list-style: none;
    margin-top: 18px;
    font-size: 15px;
    line-height: 1.3;
  }
  .contact__label {
    color: var(--brand-plum);
    margin-right: 4px;
  }
  .contact__list strong { font-weight: 700; }
  .contact__list em { font-style: italic; font-weight: 700; }
</style>
</head>
<body>
<main class="canvas">
  <section class="card card--front" aria-label="Business card front">
    <div class="front-brand">
      <span class="wordmark"><span class="wordmark__dot"></span>bright fern co</span>
    </div>
    <p class="front-url">www.<strong>brightfernco</strong>.com.au</p>
  </section>

  <section class="card card--back" aria-label="Business card back">
    <div class="back-brand">
      <span class="wordmark"><span class="wordmark__dot"></span>bright fern co</span>
    </div>
    <div class="contact">
      <p class="contact__name">Maren Tollvey-Hart</p>
      <p class="contact__role">Director</p>
      <ul class="contact__list">
        <li><span class="contact__label">p:</span><strong>+ 61 (0) 418 556 230</strong></li>
        <li><span class="contact__label">e:</span><em>maren</em>@brightfernco.com.au</li>
        <li><span class="contact__label">w:</span>www.<strong>brightfernco</strong>.com.au</li>
      </ul>
    </div>
  </section>
</main>
</body>
</html>
```